Book "Quiet Orchards"

The cover SHOULD NOT INCLUDE Eiffel Tower and baguette (French bread)
Cover for the book: "Les Vergers calmes" (the title is in French)
Size: 21 x 27cm
Author: Circle of riverside painters & Trust for the brightest lantern makers
Publisher (at the bottom of the cover): Editions Morvane

The book is intended to show that France and its culture can please to teenagers (16 - 20 years old), ie:
- story
- villages, monuments, castles, Arc de Triomphe
- French language, literature
- French national symbol (a cockerel)
- Army
- sport and sport for the disabled
- Foreigners living in France
- art of living

Besoin de plus de jours pour examiner

Waiting for a meeting of the editors, April 14th.

youngpeople

Book

• Eiffel Tower, wand

```html
<!DOCTYPE html>
<html lang="fr">
<head>
<meta charset="utf-8">
<title>Les Vergers calmes</title>
<link rel="stylesheet" href="https://fonts.googleapis.com/css2?family=Kaushan+Script&family=Cinzel:wght@600;700&family=Catamaran:wght@300&display=swap">
<style>
  :root {
    --backdrop: #6b7a94;
    --paper: #f6f5f3;
    --gold: #b5843f;
    --ink-dark: #353c4a;
    --ink-blue: #445478;
    --ink-black: #1a1a1a;
    --wash-sky: #d9e1ec;
    --wash-stone: #dccaa6;
    --wash-ochre: #c29c68;
    --wash-ground: #d4d2cf;
  }
  html, body {
    margin: 0;
    padding: 0;
    width: 1051px;
    height: 1200px;
    overflow: hidden;
    background: var(--backdrop);
  }
  .canvas {
    position: relative;
    width: 1051px;
    height: 1200px;
  }
  .cover {
    position: absolute;
    left: 162px;
    top: 133px;
    width: 727px;
    height: 936px;
    background: var(--paper);
    overflow: hidden;
  }
  .title {
    margin: 0;
    font-weight: normal;
  }
  .title-script {
    position: absolute;
    left: 0;
    right: 0;
    text-align: center;
    font-family: 'Kaushan Script', cursive;
    line-height: 1;
  }
  .title-lead {
    top: 46px;
    font-size: 176px;
    color: var(--gold);
    transform: translateX(-10px);
  }
  .title-middle {
    top: 212px;
    font-size: 112px;
    color: var(--ink-dark);
    transform: translateX(8px);
  }
  .title-caps {
    position: absolute;
    left: 0;
    right: 0;
    top: 330px;
    text-align: center;
    font-family: 'Cinzel', serif;
    font-weight: 700;
    font-size: 94px;
    letter-spacing: 1px;
    line-height: 1;
    color: var(--ink-blue);
  }
  .illustration {
    position: absolute;
    left: 40px;
    top: 440px;
    width: 660px;
    height: 350px;
  }
  .authors {
    position: absolute;
    left: 0;
    right: 0;
    top: 810px;
    margin: 0;
    text-align: center;
    font-family: 'Cinzel', serif;
    font-weight: 700;
    font-size: 16px;
    line-height: 19px;
    letter-spacing: 0.3px;
    color: var(--ink-dark);
  }
  .publisher {
    position: absolute;
    left: 50%;
    top: 879px;
    transform: translateX(-50%);
    padding: 0 6px;
    height: 32px;
    line-height: 34px;
    background: #ffffff;
    font-family: 'Catamaran', sans-serif;
    font-weight: 300;
    font-size: 23px;
    color: var(--ink-black);
    white-space: nowrap;
  }
</style>
</head>
<body>
<div class="canvas">
  <section class="cover">
    <h1 class="title">
      <span class="title-script title-lead">Les</span>
      <span class="title-script title-middle">Vergers</span>
      <span class="title-caps">CALMES</span>
    </h1>

    <svg class="illustration" viewBox="0 0 660 350" role="img" aria-label="Watercolour illustration of a French château façade with a central arched gateway, spired chapel and domed tower above a paved forecourt">
      <defs>
        <linearGradient id="wash-tone" x1="0" y1="0" x2="0" y2="1">
          <stop offset="0" stop-color="var(--wash-sky)" stop-opacity="0.6"/>
          <stop offset="0.3" stop-color="var(--wash-sky)"/>
          <stop offset="0.5" stop-color="var(--wash-stone)"/>
          <stop offset="0.72" stop-color="var(--wash-ochre)"/>
          <stop offset="0.88" stop-color="var(--wash-ground)"/>
          <stop offset="1" stop-color="var(--paper)"/>
        </linearGradient>
        <filter id="wash-edge" x="-10%" y="-10%" width="120%" height="120%">
          <feGaussianBlur stdDeviation="9"/>
        </filter>
      </defs>
      <path filter="url(#wash-edge)" fill="url(#wash-tone)"
        d="M30 170 C40 110 120 95 200 100 C250 60 300 25 340 30 C380 30 420 60 460 70 C540 60 610 90 630 150 C645 210 640 270 600 300 C500 335 420 330 330 325 C240 335 130 335 70 305 C35 280 22 220 30 170 Z"/>
    </svg>

    <p class="authors">CIRCLE OF RIVERSIDE PAINTERS<br>&amp; TRUST FOR THE BRIGHTEST<br>LANTERN MAKERS</p>

    <div class="publisher">Editions Morvane</div>
  </section>
</div>
</body>
</html>
```